Lumen Tide flyer KQ Dive Bonaire

On Bonaire we are working on a Lumen Tide project. Growing corals and placing them on the reef, to keep the reefs healthy. KQ Dive has her own coral tree. We are giving Lumen Tide courses, so people can help us to protect the reef.
We like to have a flyer to sell these courses to our guests.
It needs to be informative and appealing for divers to participate.

Target Market(s)

Divers

Industry/Entity Type

Diving / tourism industry

Font styles to use
Sans Serif

Colors
0054AA
0677BA
7BADD7
CADEEF
E8F1F8
F0912C
F2A743
F7CA91
FBE8D2
FDF5EE

Requirements
Must have
• The pictures we added as attachment
Should not have
• No pictures not from Bonaire

```html
<!DOCTYPE html>
<html lang="en">
<head>
<meta charset="utf-8">
<title>Lumen Tide flyers – KQ Dive Bonaire</title>
<link rel="stylesheet" href="https://fonts.googleapis.com/css2?family=Jost:wght@500;600;700;800&display=swap">
<style>
  :root {
    --navy: #0054AA;
    --blue: #0677BA;
    --sky: #7BADD7;
    --ice: #CADEEF;
    --mist: #E8F1F8;
    --orange: #F0912C;
    --amber: #F2A743;
    --peach: #F7CA91;
    --cream: #FBE8D2;
    --shell: #FDF5EE;
    --band: #3F66B3;
    --teal: #3BB9C9;
    --page: #EEF2F5;
  }
  * { box-sizing: border-box; margin: 0; padding: 0; }
  html, body { width: 1200px; height: 800px; overflow: hidden; }
  body {
    background: var(--page);
    font-family: "Jost", sans-serif;
    position: relative;
  }
  .flyer {
    position: absolute;
    top: 45px;
    width: 500px;
    height: 710px;
    overflow: hidden;
    background: #DCEBF5;
    box-shadow: 0 8px 24px rgba(0, 40, 80, 0.15);
  }

  /* ---------- Discover dive flyer ---------- */
  .flyer--discover { left: 60px; }
  .discover__band {
    position: absolute; left: 0; top: 0; bottom: 0; width: 56px;
    background: var(--band);
    display: flex; align-items: center; justify-content: center;
  }
  .discover__band-title {
    writing-mode: vertical-rl;
    transform: rotate(180deg);
    font-weight: 800;
    font-size: 40px;
    letter-spacing: 1px;
    color: var(--amber);
    white-space: nowrap;
  }
  .discover__band-title .accent { color: var(--peach); }
  .discover__photo {
    position: absolute; left: 56px; top: 0; width: 444px; height: 360px;
  }
  .discover__brand {
    position: absolute; right: 30px; top: 372px;
    font-weight: 700; font-size: 20px; color: var(--navy);
  }
  .discover__headline {
    position: absolute; left: 180px; top: 400px; width: 300px;
    font-weight: 800; font-size: 42px; line-height: 0.98;
    color: var(--orange);
  }
  .discover__cta {
    position: absolute; left: 90px; top: 600px; width: 390px;
    font-weight: 600; font-size: 21px; line-height: 1.05;
    color: var(--navy); text-align: center;
  }
  .discover__note {
    position: absolute; left: 90px; top: 660px; width: 390px;
    font-weight: 600; font-size: 10.5px; letter-spacing: 0.2px;
    color: var(--orange); text-align: center;
  }

  /* ---------- Specialty flyer ---------- */
  .flyer--specialty { left: 640px; background: #D9E8F4; }
  .specialty__shape { position: absolute; inset: 0; }
  .specialty__title {
    position: absolute; left: 28px; top: 36px; width: 460px;
    font-weight: 800; font-size: 30px; line-height: 1.05;
    color: var(--navy);
  }
  .specialty__headline {
    position: absolute; left: 50px; top: 150px;
    font-weight: 800; font-size: 50px; line-height: 1.02;
    color: var(--shell);
  }
  .specialty__photo {
    position: absolute; border-radius: 50%;
  }
  .specialty__photo--diver { left: 320px; top: 100px; width: 170px; height: 170px;
    background: radial-gradient(circle at 50% 30%, #6E8FB8, #2F4E80 60%, #B27A52 100%); }
  .specialty__photo--tree { left: 282px; top: 272px; width: 176px; height: 176px;
    background: radial-gradient(circle at 40% 40%, #7FA7C7, #1F4C7C 75%); }
  .specialty__photo--coral { left: 345px; top: 420px; width: 150px; height: 150px;
    background: radial-gradient(circle at 50% 65%, #A68460, #4E7DA6 70%); }
  .specialty__intro {
    position: absolute; left: 36px; top: 520px; width: 300px;
    font-weight: 700; font-size: 16px; line-height: 1.25;
    color: var(--navy);
  }
  .specialty__facts {
    position: absolute; left: 36px; top: 572px; width: 360px;
    font-weight: 700; font-size: 17px; line-height: 1.5;
    color: var(--orange);
  }
  .specialty__num {
    display: inline-flex; align-items: center; justify-content: center;
    width: 34px; height: 34px; border-radius: 50%;
    background: var(--teal); color: var(--shell);
    font-size: 22px; vertical-align: middle; margin: 0 4px;
  }
  .specialty__social {
    position: absolute; right: 24px; top: 590px;
    display: flex; gap: 12px;
    font-weight: 600; font-size: 11px; color: var(--navy);
  }
  .specialty__partners {
    position: absolute; left: 36px; right: 24px; top: 650px;
    display: flex; align-items: center; justify-content: space-between;
  }
  .badge--island { width: 110px; height: 40px; background: var(--shell); border: 1px solid var(--ice); }
  .badge--cert { width: 42px; height: 42px; background: var(--shell); border: 1px solid var(--ice); }
  .specialty__brand {
    font-weight: 700; font-size: 18px; color: var(--navy);
  }
</style>
</head>
<body>

<article class="flyer flyer--discover">
  <svg class="discover__photo" viewBox="0 0 444 360" role="img" aria-label="Underwater photo of elkhorn coral on a sandy Bonaire reef">
    <defs>
      <linearGradient id="sea" x1="0" y1="0" x2="0" y2="1">
        <stop offset="0" stop-color="#1E7E93"/>
        <stop offset="0.45" stop-color="#6FB9BE"/>
        <stop offset="0.75" stop-color="#B9A088"/>
        <stop offset="1" stop-color="#A8887A"/>
      </linearGradient>
    </defs>
    <path d="M0 0 H444 V330 L330 338 Q200 300 0 260 Z" fill="url(#sea)"/>
    <path d="M0 260 Q200 300 330 338 L444 330 V360 H0 Z" fill="#CFE3F0"/>
  </svg>

  <div class="discover__band">
    <h2 class="discover__band-title">DISCOVER <span class="accent">LUMEN TIDE</span> DIVE</h2>
  </div>

  <div class="discover__brand">KQ Dive</div>

  <h1 class="discover__headline">WANT TO LEARN MORE ABOUT OUR REEF?</h1>
  <p class="discover__cta">PARTICIPATE IN OUR<br>DISCOVER LUMEN TIDE DIVE!</p>
  <p class="discover__note">IN HALF A DAY WE SHOW YOU WHAT WE DO TO HELP OUR REEF</p>
</article>

<article class="flyer flyer--specialty">
  <svg class="specialty__shape" viewBox="0 0 500 710" aria-hidden="true">
    <path d="M0 0 H500 V120 Q420 60 0 110 Z" fill="var(--amber)"/>
    <path d="M0 110 Q420 60 500 120 V300 Q420 470 300 480 L0 480 Z" fill="var(--orange)"/>
    <path d="M0 480 L300 480 Q200 500 0 500 Z" fill="var(--orange)"/>
  </svg>

  <h2 class="specialty__title">LUMEN TIDE DIVER<br>DISTINCTIVE SPECIALTY</h2>
  <h1 class="specialty__headline">HELP<br>RESTORE<br>OUR<br>REEFS!</h1>

  <div class="specialty__photo specialty__photo--diver" role="img" aria-label="Diver tending staghorn coral on the reef"></div>
  <div class="specialty__photo specialty__photo--tree" role="img" aria-label="Diver working at a coral tree nursery"></div>
  <div class="specialty__photo specialty__photo--coral" role="img" aria-label="Restored staghorn coral on the Bonaire reef"></div>

  <p class="specialty__intro">Become an active member<br>in helping restore our reef.</p>
  <p class="specialty__facts">In<span class="specialty__num">2</span>days and<span class="specialty__num">3</span>dives<br>you learn all about the reef of Bonaire</p>

  <div class="specialty__social"><span>Shoreline</span><span>Tidepost</span></div>

  <div class="specialty__partners">
    <div class="badge--island" role="img" aria-label="Island tourism partner badge"></div>
    <div class="badge--cert" role="img" aria-label="Dive certification badge"></div>
    <div class="specialty__brand">KQ Dive</div>
  </div>
</article>

</body>
</html>
```